Hi Corinna, we need our wine labels produced for this year's vintage with a few changes. We would like to keep the integrity of the current label for the H and want the blue and gold to remain in the design. However we would like to include an image of a tree and our dogs.

```html
<!DOCTYPE html>
<html lang="en">
<head>
<meta charset="utf-8">
<title>Marlowe Ridge – Fenwick's Paddock Pinot Noir 2019</title>
<link rel="stylesheet" href="https://fonts.googleapis.com/css2?family=Arimo:wght@400;700&family=EB+Garamond:ital,wght@1,400&display=swap">
<style>
  :root {
    --page: #eef0f1;
    --label: #ffffff;
    --navy: #23266b;
    --navy-script: #1c1f5e;
    --gold: #7f6726;
    --gold-light: #a88d3c;
    --ink: #111111;
    --tree-dark: #2a2a2a;
    --tree-light: #d9d9d9;
  }
  * { margin: 0; padding: 0; box-sizing: border-box; }
  html, body {
    width: 1200px;
    height: 923px;
    overflow: hidden;
    background: var(--page);
  }
  .wine-label {
    position: absolute;
    left: 246px;
    top: 138px;
    width: 708px;
    height: 646px;
    background: var(--label);
    overflow: hidden;
    font-family: "Arimo", Arial, sans-serif;
    color: var(--ink);
  }
  .band-pattern-top {
    position: absolute;
    left: 0; top: 0;
    width: 100%; height: 88px;
    background: var(--navy);
  }
  .band-pattern-gold {
    position: absolute;
    left: 0;
    width: 100%;
    background: linear-gradient(var(--gold-light), var(--gold));
  }
  .band-pattern-gold.top { top: 88px; height: 22px; }
  .band-pattern-gold.bottom { bottom: 0; height: 35px; }
  .crest-arch {
    position: absolute;
    left: 288px;
    top: 36px;
    width: 134px;
    height: 134px;
    border-radius: 50%;
    background: var(--label);
  }
  .crest-name {
    position: absolute;
    left: 288px;
    top: 70px;
    width: 134px;
    text-align: center;
    font-weight: 700;
    font-size: 20px;
    color: var(--gold);
    letter-spacing: 0.5px;
  }
  .estate-name {
    position: absolute;
    left: 0; top: 118px;
    width: 100%;
    text-align: center;
    font-weight: 700;
    font-size: 44px;
    line-height: 44px;
    color: var(--gold);
    letter-spacing: 0.5px;
  }
  .range-name {
    position: absolute;
    left: 0; top: 166px;
    width: 100%;
    text-align: center;
    font-family: "EB Garamond", Georgia, serif;
    font-style: italic;
    font-size: 48px;
    line-height: 52px;
    color: var(--navy-script);
  }
  .tree-illustration {
    position: absolute;
    left: 185px;
    top: 235px;
    width: 342px;
    height: 273px;
  }
  .varietal {
    position: absolute;
    left: 0; top: 529px;
    width: 100%;
    text-align: center;
    font-weight: 700;
    font-size: 24px;
    line-height: 26px;
  }
  .vintage {
    position: absolute;
    left: 0; top: 557px;
    width: 100%;
    text-align: center;
    font-weight: 700;
    font-size: 24px;
    line-height: 26px;
  }
  .region {
    position: absolute;
    left: 0; top: 590px;
    width: 100%;
    text-align: center;
    font-weight: 700;
    font-size: 17px;
    line-height: 20px;
  }
  .preservative {
    position: absolute;
    left: 8px; top: 593px;
    font-size: 13px;
    line-height: 16px;
  }
  .volume, .alcohol {
    position: absolute;
    right: 11px;
    font-size: 15px;
    line-height: 18px;
    text-align: right;
  }
  .volume { top: 568px; }
  .alcohol { top: 591px; }
</style>
</head>
<body>
  <main class="wine-label">
    <div class="band-pattern-top" role="img" aria-label="Navy chevron zigzag pattern band"></div>
    <div class="band-pattern-gold top" role="img" aria-label="Gold chevron zigzag pattern band"></div>
    <div class="crest-arch"></div>
    <div class="crest-name">Marlowe</div>

    <h1 class="estate-name">MARLOWE RIDGE</h1>
    <h2 class="range-name">Fenwick’s Paddock</h2>

    <svg class="tree-illustration" viewBox="0 0 342 273" role="img" aria-label="Pen sketch of a tall pine tree on a hill with two small dogs running beneath it">
      <defs>
        <radialGradient id="treeTone" cx="50%" cy="45%" r="60%">
          <stop offset="0%" stop-color="var(--tree-dark)"/>
          <stop offset="100%" stop-color="var(--tree-light)"/>
        </radialGradient>
      </defs>
      <rect width="342" height="273" fill="url(#treeTone)"/>
    </svg>

    <p class="varietal">PINOT NOIR</p>
    <p class="vintage">2019</p>
    <p class="region">MORNINGTON PENINSULA</p>
    <p class="preservative">Preservative 220 added</p>
    <p class="volume">750 ml</p>
    <p class="alcohol">ALC/VOL 14.8%</p>

    <div class="band-pattern-gold bottom" role="img" aria-label="Gold chevron zigzag pattern band"></div>
  </main>
</body>
</html>
```